advertising board Morvalen BV

I have an advertisement spot in a small indoor football stadium, with the size of 1.00 x 22.00 meters. I want to show a design that stands out. My company works in Civil constructions and actually installs steel sheet piles and earth retaining walls in the most difficult to reach locations.

```html
<!DOCTYPE html>
<html lang="nl">
<head>
<meta charset="utf-8">
<title>Morvalen BV – reclamebord</title>
<link href="https://fonts.googleapis.com/css2?family=Ubuntu:wght@400&display=swap" rel="stylesheet">
<style>
  :root {
    --page-bg: #ffffff;
    --board-blue-light: #bfe2f8;
    --board-blue-dark: #4aaee3;
    --board-white: #ffffff;
    --ink: #34343a;
    --scene-cream: #f8f4d2;
    --scene-cream-edge: #efe8b8;
    --scene-ground: #8a5a36;
    --shadow: rgba(0, 0, 0, 0.35);
  }
  html, body {
    margin: 0;
    padding: 0;
    width: 1200px;
    height: 1000px;
    overflow: hidden;
    background: var(--page-bg);
  }
  .canvas {
    position: relative;
    width: 1200px;
    height: 1000px;
  }
  .board {
    position: absolute;
    left: 35px;
    width: 1130px;
    height: 205px;
    overflow: hidden;
  }
  .board--blue {
    top: 242px;
    background: linear-gradient(90deg, var(--board-blue-light) 0%, #9fd2f2 40%, var(--board-blue-dark) 100%);
  }
  .board--white {
    top: 555px;
    background: var(--board-white);
    box-shadow: 4px 6px 6px var(--shadow);
    outline: 1px solid #eeeeee;
  }
  .board__scene {
    position: absolute;
    left: 3px;
    top: 8px;
    width: 262px;
    height: 262px;
    border-radius: 50%;
    background: radial-gradient(circle at 50% 45%, var(--scene-cream) 0%, var(--scene-cream) 60%, var(--scene-cream-edge) 100%);
  }
  .board__ground {
    position: absolute;
    left: 20px;
    top: 201px;
    width: 232px;
    height: 4px;
    background: var(--scene-ground);
  }
  .board__name {
    position: absolute;
    left: 276px;
    top: 10px;
    margin: 0;
    font-family: "Ubuntu", sans-serif;
    font-weight: 400;
    font-size: 134px;
    line-height: 1;
    letter-spacing: 2px;
    color: var(--ink);
    white-space: nowrap;
  }
  .board__services {
    position: absolute;
    left: 277px;
    top: 142px;
    margin: 0;
    font-family: "Ubuntu", sans-serif;
    font-weight: 400;
    font-size: 26.5px;
    line-height: 1;
    color: var(--ink);
    white-space: nowrap;
  }
</style>
</head>
<body>
<main class="canvas">
  <section class="board board--blue">
    <div class="board__scene" role="img" aria-label="Illustratie van een bouwplaats met fabriek, torenkraan, graafmachine en zandhoop voor een zon"></div>
    <div class="board__ground"></div>
    <h1 class="board__name">Morvalen BV</h1>
    <p class="board__services">damwandconstructies - onderhoud - beschoeiingen - grondwerk</p>
  </section>

  <section class="board board--white">
    <div class="board__scene" role="img" aria-label="Illustratie van een bouwplaats met fabriek, torenkraan, graafmachine en zandhoop voor een zon"></div>
    <div class="board__ground"></div>
    <h2 class="board__name">Morvalen BV</h2>
    <p class="board__services">damwandconstructies - onderhoud - beschoeiingen - grondwerk</p>
  </section>
</main>
</body>
</html>
```